IT Tradingsystem for car dealers needs Business Card Design

We need a fresh and modern design for our new business cards.

We develop a it-business system for car dealers in Sweden, Norway and on our way down to further countries in Europe, hence the namechange to BrolaTek Europe AB. The site can be found at www.brolatek-example.com. The startpage is also in for an update/modernization soon so don't take to much from here.

We are looking to print double sided, 4-colour cards.

We want to look professional, modern and serious. Open to cooler suggestions, but not too crazy. We need to make a good and serious impression on our potential customers. It needs to reflect our scandinavian design values and layout.

Preferably with the full BrolaTek logo in good size on the back, so the small print on the logo can be read easily.

Text that needs to go on the cards:
-------

Per Oskar Fjellström
Founder

Direct +46 70-512 96 47
Support 08-612 57 394
po.fjellstrom@brolatek-example.com

BrolaTek Europe AB
Box 8617
104 29 Stockholm

Brolatek-example.com
Saljportalen-example.se

--------
Good luck and thanks!

PS. If you need more input or see what our previous cards looked like, don't hesitate to contact me!

Target Market(s)

Decision makers / executives at brand cardealers

Industry/Entity Type

Automotive

Contact Information for Business Card

Normal size

Requirements
Must have
• Full logo
Nice to have
• Base on our orange colors
Should not have
• No fonts with serif, and not too much graphics

```html
<!DOCTYPE html>
<html lang="sv">
<head>
<meta charset="utf-8">
<title>BrolaTek – Business Card</title>
<link href="https://fonts.googleapis.com/css2?family=Montserrat:wght@400;500;600;700&display=swap" rel="stylesheet">
<style>
  :root {
    --navy: #0f2f40;
    --navy-light: #1c4456;
    --orange: #f47b20;
    --orange-soft: #f7a05a;
    --white: #ffffff;
    --ink: #13232d;
    --backdrop: #e4e6e8;
  }
  * { box-sizing: border-box; margin: 0; padding: 0; }
  html, body {
    width: 1200px; height: 742px; overflow: hidden;
    background: var(--backdrop);
    font-family: "Montserrat", sans-serif;
  }
  .sheet {
    width: 1200px; height: 742px;
    display: flex; align-items: center; justify-content: center; gap: 40px;
  }
  .card {
    position: relative;
    width: 540px; height: 309px;
    border-radius: 22px;
    overflow: hidden;
    box-shadow: 0 6px 18px rgba(0,0,0,0.12);
  }

  /* Front */
  .card-front {
    background: linear-gradient(120deg, var(--navy) 0%, var(--navy-light) 50%, var(--navy) 100%);
    display: flex; flex-direction: column; align-items: center; justify-content: center;
  }
  .brand {
    display: flex; align-items: center; gap: 14px;
  }
  .brand-square {
    width: 34px; height: 34px; background: var(--orange);
  }
  .brand-name {
    color: var(--white); font-weight: 700; font-size: 50px; letter-spacing: -0.5px;
  }
  .tagline {
    margin-top: 8px;
    color: var(--orange); font-weight: 500; font-size: 11.5px; letter-spacing: 0.6px;
  }

  /* Back */
  .card-back { background: var(--white); }
  .back-panel { position: absolute; inset: 0; }
  .back-brand {
    position: absolute; left: 34px; top: 110px;
    color: var(--orange); font-weight: 700; font-size: 34px;
  }
  .back-sites {
    position: absolute; left: 36px; top: 214px;
    color: var(--orange); font-weight: 500; font-size: 13px; line-height: 1.2;
  }
  .contact {
    position: absolute; left: 312px; top: 40px; width: 212px;
    color: var(--ink);
  }
  .person-name {
    display: flex; align-items: center; gap: 6px;
    font-weight: 700; font-size: 12.5px; letter-spacing: 2px; white-space: nowrap;
  }
  .person-role {
    display: flex; align-items: center; gap: 8px;
    margin-top: 2px;
    font-weight: 700; font-size: 12.5px; letter-spacing: 2px;
  }
  .rule { height: 2px; background: var(--orange); flex: 1; }
  .rule-short { height: 2px; background: var(--orange); width: 60px; }
  .details { margin-top: 14px; list-style: none; }
  .details li {
    display: flex; align-items: flex-start; gap: 8px;
    font-size: 10.5px; line-height: 1.45; white-space: nowrap;
  }
  .details .icon { width: 12px; height: 12px; margin-top: 2px; flex: none; }
  .details .text { line-height: 1.45; }
</style>
</head>
<body>
<main class="sheet">

  <section class="card card-front" aria-label="Card front">
    <div class="brand">
      <span class="brand-square"></span>
      <span class="brand-name">BrolaTek</span>
    </div>
    <p class="tagline">KorTest | Remarketing | saljportalen-example.se</p>
  </section>

  <section class="card card-back" aria-label="Card back">
    <svg class="back-panel" viewBox="0 0 540 309" width="540" height="309" aria-hidden="true">
      <polyline points="200,0 312,150 226,309" fill="none" stroke="#f47b20" stroke-width="3"/>
      <defs>
        <linearGradient id="panelShade" x1="0" y1="0" x2="1" y2="0.4">
          <stop offset="0" stop-color="#0f2f40"/>
          <stop offset="0.7" stop-color="#1c4456"/>
          <stop offset="1" stop-color="#0f2f40"/>
        </linearGradient>
      </defs>
      <polygon points="0,0 192,0 302,150 218,309 0,309" fill="url(#panelShade)"/>
    </svg>

    <div class="back-brand">BrolaTek</div>
    <p class="back-sites">Brolatek-example.com<br>Saljportalen-example.se</p>

    <div class="contact">
      <p class="person-name"><span>Per Oskar Fjellström</span><span class="rule"></span></p>
      <p class="person-role"><span class="rule-short"></span><span>Founder</span></p>

      <ul class="details">
        <li>
          <svg class="icon" viewBox="0 0 12 12" aria-hidden="true"><path d="M2.5 1 4.5 3 3.6 4.4c.6 1.5 1.8 2.8 3.4 3.5L8.4 7 10.5 9 9.3 10.6C5.4 10.4 1.6 6.6 1.2 2.4Z" fill="#13232d"/></svg>
          <span class="text">+46 70-512 96 47</span>
        </li>
        <li>
          <svg class="icon" viewBox="0 0 12 12" aria-hidden="true"><ellipse cx="6" cy="5.2" rx="5" ry="3.8" fill="#13232d"/><path d="M3 8 2 11 5.5 8.6Z" fill="#13232d"/></svg>
          <span class="text">08-612 57 394</span>
        </li>
        <li>
          <svg class="icon" viewBox="0 0 12 12" aria-hidden="true"><rect x="0.8" y="2.5" width="10.4" height="7" fill="#13232d"/><path d="M1 2.8 6 6.6 11 2.8" fill="none" stroke="#fff" stroke-width="1"/></svg>
          <span class="text">po.fjellstrom@brolatek-example.com</span>
        </li>
        <li>
          <svg class="icon" viewBox="0 0 12 12" aria-hidden="true"><path d="M6 1 11.2 5.8H9.6V11H7.2V8H4.8V11H2.4V5.8H0.8Z" fill="#13232d"/></svg>
          <span class="text">BrolaTek Europe AB<br>Box 8617<br>104 29 Stockholm</span>
        </li>
      </ul>
    </div>
  </section>

</main>
</body>
</html>
```